Poster for Dance Choreography Workshop

We need a poster for a dance workshop. This workshop is unique in that instead of focusing on dance technique or on classical compositional practices, it teaches participants a toolbox of a collaborative, improvisational methods for generating movement and creating dances.

The workshop is called VERIL (Methods for Exploring Gesture and Dancemaking). Our dance company is Helen Dorsey & Ensemble.

Here is copy:
VERIL (Methods for Exploring Gesture and Dancemaking) is a six-day intensive led by Helen Dorsey & Ensemble in which dancers and choreographers investigate collaborative approaches to choreography. Each day begins with an hour-long presentation during which Helen Dorsey leads discussions on topics related to choreography and collaboration. Following this, Helen Dorsey and VERIL company members teach a variety of practices for collaborative movement-making that merge improvisational skills with contemporary dance technique and physical theater. Using these practices, participants will create miniature compositions in small groups each day. By examining and discussing these creations, participants leave with greater confidence in their creative abilities and a deeper understanding of composition and movement-making.
This intensive, hosted at Whitcombe College in NYC, brings together a wide variety of talented dance artists and provides them with a supportive environment in which to play, learn, experiment and share. The intensive also affords an exciting opportunity for building peer-communities and forging new creative bonds. VERIL’s goal is that all participants leave with fresh perspectives, tools they can immediately use in their own rehearsals, and a better understanding of their own creative processes.

DATES:
June 11—June 16, 2012
10:00am—6:00pm daily
LOCATION:
Department of Dance,
Whitcombe College of
Harrowgate University
4127 Linden Avenue at 82nd
New York, NY 10094
Housing is not available.
Company teachers:
Helen Dorsey
Maribeth Quennell
Owen Patch
Toby Renfield

Special presentation by
Greta L. Fenwick,
Tall Stage Collective

Applications available online at www.helendorseyensemble.org or email veril@verilworks.org.
Application deadline April 1, 2012.

Hello all,

Nice work so far!
Please note that I have high resolution version of the images in the brief available. I did not include them because of the bandwidth of my connection. If you would like some of the images in higher res (5616x3744) let me know and I can provide them.

Best,

Colin

Target Market(s)

College-age and above. Professional dancers.

Industry/Entity Type

Environment

Requirements
Must have
• Poster must be 11x17 or smaller.
Visit www.northernmovementfair.org, www.pkthf.org, www.vlxmotion.org for competitors. Should not be easy to confuse with these.

```html
<!DOCTYPE html>
<html lang="en">
<head>
<meta charset="utf-8">
<title>VERIL — Dance Choreography Workshop</title>
<link href="https://fonts.googleapis.com/css2?family=Didact+Gothic&display=swap" rel="stylesheet">
<style>
  :root {
    --paper: #ffffff;
    --magenta: #9c2f63;
    --magenta-band: rgba(150, 40, 95, 0.78);
    --photo-light: #e6e3e3;
    --photo-mid: #b9b5b6;
    --photo-dark: #6f6a6c;
    --ink: #2a2a2a;
    --band-text: #ffffff;
  }
  html, body { margin: 0; padding: 0; overflow: hidden; }
  body { width: 802px; height: 1200px; background: var(--paper); font-family: "Didact Gothic", "Helvetica Neue", Arial, sans-serif; }
  .poster { position: relative; width: 802px; height: 1200px; overflow: hidden; background: var(--paper); }
  .photo {
    position: absolute; left: 32px; top: 0; width: 738px; height: 1120px;
    background:
      radial-gradient(ellipse 38% 30% at 70% 20%, var(--photo-dark) 0%, transparent 70%),
      radial-gradient(ellipse 30% 45% at 40% 72%, var(--photo-mid) 0%, transparent 75%),
      radial-gradient(ellipse 25% 30% at 85% 65%, var(--photo-mid) 0%, transparent 75%),
      linear-gradient(180deg, var(--paper) 0%, var(--photo-light) 45%, #d5d1d2 100%);
  }
  .title {
    position: absolute; left: 40px; top: 30px; margin: 0;
    font-weight: 400; font-size: 90px; letter-spacing: 4px; color: var(--magenta);
  }
  .band {
    position: absolute; left: 32px; top: 210px; width: 738px; height: 500px;
    background: var(--magenta-band);
  }
  .about {
    position: absolute; left: 60px; top: 228px; width: 410px;
    color: var(--band-text); font-size: 11.4px; line-height: 1.42;
  }
  .about h2 { margin: 0 0 10px; font-size: 14px; font-weight: 400; line-height: 1.3; }
  .about p { margin: 0; }
  .details {
    position: absolute; left: 505px; top: 320px; width: 250px; text-align: right;
    color: var(--band-text);
  }
  .dates { font-size: 20px; line-height: 1.25; margin: 0 0 28px; }
  .teachers, .special { font-size: 15.5px; line-height: 1.3; margin: 0 0 22px; }
  .footer {
    position: absolute; left: 32px; top: 1140px; width: 738px;
    font-size: 8.6px; line-height: 1.4; color: var(--ink); margin: 0;
  }
</style>
</head>
<body>
<main class="poster">
  <div class="photo" role="img" aria-label="Black and white photograph of dancers in a studio, arms raised and bodies leaning together"></div>
  <h1 class="title">VERIL</h1>
  <div class="band"></div>
  <section class="about">
    <h2>Methods for Exploring Gesture and<br>Dancemaking</h2>
    <p>is a six-day intensive led by Helen Dorsey &amp; Ensemble in which dancers and choreographers investigate collaborative approaches to choreography. Each day begins with an hour-long presentation during which Helen Dorsey leads discussions on topics related to choreography and collaboration. Following this, Helen Dorsey and VERIL company members teach a variety of practices for collaborative movement-making that merge improvisational skills with contemporary dance technique and physical theater. Using these practices, participants will create miniature compositions in small groups each day. By examining and discussing these creations, participants leave with greater confidence in their creative abilities and a deeper understanding of composition and movement-making.</p>
    <p>This intensive, hosted at Whitcombe College in NYC, brings together a wide variety of talented dance artists and provides them with a supportive environment in which to play, learn, experiment and share. The intensive also affords an exciting opportunity for building peer-communities and forging new creative bonds. VERIL’s goal is that all participants leave with fresh perspectives, tools they can immediately use in their own rehearsals, and a better understanding of their own creative processes.</p>
  </section>
  <section class="details">
    <p class="dates">June 11 — June 16, 2012<br>10:00am — 6:00pm daily</p>
    <p class="teachers">Company teachers:<br>Helen Dorsey<br>Maribeth Quennell<br>Owen Patch<br>Toby Renfield</p>
    <p class="special">Special presentation by<br>Greta L. Fenwick,<br>Tall Stage Collective</p>
  </section>
  <p class="footer">Department of Dance, Whitcombe College of Harrowgate University 4127 Linden Avenue at 82nd New York, NY 10094 Housing is not available. Applications available online at www.helendorseyensemble.org or email veril@verilworks.org<br>Application deadline April 1, 2012.</p>
</main>
</body>
</html>
```